Dietetic office: Bright Plate

I want to give my business card a modern and warm look (which attracts the eye and has a reassuring side), which links dietetics to a moment of well-being. The front and back sides must be used (not just to put the logo on the front side)

The map should be eye-catching and easy to read. I don't necessarily want to have a plain background, which I find visually weighs down the maps.
I really like the square format of a business card with rounded edges which is different from what we are used to finding (and why not take this square diagonally?), however I am not closed to another format as long as I like the style.

Who am I? Mireille, 32 years old, Dietician and passionate about food since always. I am specialized in slimming and an expert in micro nutrition, which means that I take into account not only the nutritional balance while maintaining pleasure (if foods are present in the business card, I do not want some cliché things where there would just be fruits and vegetables, but really something more global), but also the psycho-emotional dimension that I will treat with food supplements based on plants, fruits or vegetables.

-----------------------------------------------------------------------------------

 Mention to appear on the card IN FRENCH (please be careful in case of translation that the use of words is correct):

Mireille DORAN
Dietician Nutritionist
Expert in Slimming and Micro-Nutrition

Slogan: I help you lose weight sustainably with pleasure and by reconciling your events

Catchphrases: Want to lose weight? Do you like going out? Do you have a lot of events? And is pleasure on your plate important to you?

Make an appointment on Rendiplan or on 06 41 58 30 92
mireille.brightplate@exemplo-mail.fr
Address: Health Center, Rue des Glycines, 13990 Valbelle
www.brightplate-exemple.fr
Friendwall + Picturo Logo

- The company logo has been uploaded for your viewing. Other file formats can be made available if required.
- I would like a place for a photo of me to be possible.

Good morning,
I want to have a business card that is both lively and warm. Which will easily catch the eye while being easy to read and make people understand that I am in the field of well-being.
I like the square side in business cards (and why not use them diagonally?), or a more classic but original one.
Both the front and back sides must be used (I don't want to have the logo on just one side)
I don't want to have a plain background, but rather something more muted (I really like the suggestion from "Reed Cloud Graphic Designer" for this)
the use of logo for telephone, mail, address, rendiplan, friendwall, pictu etc is possible in order to facilitate reading

Please follow the various elements of the brief regarding the text and use the French text as it is.

I like business cards preferably square (with the possibility of using them diagonally).
The map should be eye-catching and easy to read.
It must bring pep while having softness which brings back to the well-being side
The card must be used on the front and back for the different elements (I do not want to have only the logo on the front side)
The text must correspond to the brief (be careful with the translation which can sometimes be bad)
I don't want to have a plain blue or orange background. I really like the idea of the background from "Reed Cloud Graphic Designer"

You can if you wish use symbols for contacts, telephone, rendiplan, address, fw, pictu....

Target Market(s)

mainly women between 25 and 65 years old + men around 40 years old

Contact Information for Business Card

Font styles to use
Sans Serif
Script

Colors
0054AA
0677BA
7BADD7
CADEEF
E8F1F8
0094D4
00A9DD
6FCCEA
C7EBF8
E9F6FB
00AB8E
00BBA5
67D7C9
C6EFE9
E9F9F6
FFC000
F8CF3A
FAE287
FDF2CF
FEFAEE
F0912C
F2A743
F7CA91
FBE8D2
FDF5EE

Requirements
Must have
• some pep! while being refined
Nice to have
• I really like the square format of a business card with rounded edges which is different from what we are used to finding, however I am not closed to another format as long as I like the style.
Should not have
• if foods are represented, only show fruits and vegetables (too cliché)

```html
<!DOCTYPE html>
<html lang="en">
<head>
<meta charset="utf-8">
<title>Bright Plate – Business Card</title>
<link rel="stylesheet" href="https://fonts.googleapis.com/css2?family=EB+Garamond&family=Parisienne&family=Montserrat:wght@400;600;700&display=swap">
<style>
  :root {
    --backdrop: #979797;
    --blue: #087bd7;
    --blue-deep: #0054aa;
    --name-blue: #0677ba;
    --orange: #ff9500;
    --accent-orange: #f7a02f;
    --white: #ffffff;
    --grey-text: #8e8e8e;
    --photo-grey: #c6c6c6;
  }
  * { margin: 0; padding: 0; box-sizing: border-box; }
  html, body { width: 1200px; height: 1000px; overflow: hidden; }
  body { background: var(--backdrop); position: relative; font-family: "Montserrat", sans-serif; }

  .card {
    position: absolute;
    width: 520px; height: 520px;
    border-radius: 42px;
    overflow: hidden;
    box-shadow: 10px 14px 18px rgba(0,0,0,0.35);
  }

  /* Front: catchphrases */
  .card-front { left: 72px; top: 243px; background: var(--blue); }
  .cutlery-decoration {
    position: absolute; left: 200px; top: 290px; width: 320px; height: 230px;
    background: radial-gradient(ellipse at 60% 60%, rgba(0,84,170,0.35), rgba(0,84,170,0) 70%);
  }
  .catchphrases {
    position: absolute; left: 45px; top: 48px;
    font-family: "EB Garamond", serif; color: var(--white);
    font-size: 36px; line-height: 1;
  }
  .catchphrases p { height: 50px; white-space: nowrap; }
  .catchphrases p.gap { margin-top: 12px; }
  .catchphrases p.tight { height: 48px; }
  .catchphrases em {
    font-family: "Parisienne", cursive; font-style: normal;
    color: var(--accent-orange); font-size: 48px;
  }
  .front-brand {
    position: absolute; left: 50px; top: 395px;
    font-family: "Montserrat", sans-serif; font-weight: 600;
    font-size: 36px; color: var(--white); white-space: nowrap;
  }
  .front-links {
    position: absolute; left: 308px; top: 398px; width: 200px;
    text-align center; color: var(--white);
    text-align: center;
  }
  .website { font-weight: 700; font-size: 13.5px; color: var(--accent-orange); white-space: nowrap; }
  .socials {
    margin-top: 14px; font-size: 13px; font-weight: 600;
    display: flex; justify-content: center; gap: 12px; white-space: nowrap;
  }

  /* Back: contact */
  .card-back { left: 621px; top: 241px; background: var(--white); }
  .wave { position: absolute; left: 0; top: 0; }
  .back-brand {
    position: absolute; left: 47px; top: 64px;
    font-weight: 600; font-size: 28px; color: var(--name-blue); white-space: nowrap;
  }
  .person-name {
    position: absolute; left: 47px; top: 146px;
    font-weight: 700; font-size: 20px; letter-spacing: 1.2px; color: var(--name-blue);
  }
  .person-title {
    position: absolute; left: 47px; top: 176px;
    font-size: 15.5px; line-height: 23px; color: var(--grey-text);
  }
  .photo-slot {
    position: absolute; left: 280px; top: 35px; width: 202px; height: 202px;
    border-radius: 50%; background: var(--photo-grey);
  }
  .appointment {
    position: absolute; left: 44px; top: 318px;
    font-weight: 700; font-size: 22px; line-height: 28px; color: var(--white);
  }
  .contact-list {
    position: absolute; left: 46px; top: 384px; list-style: none;
    color: var(--white); font-size: 17.5px; line-height: 25px;
  }
  .contact-list li { display: flex; align-items: flex-start; }
  .contact-list svg { width: 20px; height: 20px; margin: 2px 14px 0 0; flex: none; }
</style>
</head>
<body>

<section class="card card-front">
  <div class="cutlery-decoration" role="img" aria-label="Faint cutlery decoration in deep blue"></div>
  <div class="catchphrases">
    <p>Want to <em>lose</em> weight?</p>
    <p>Do you like <em>going out</em>?</p>
    <p class="gap">Do you have a lot of <em>events</em>?</p>
    <p class="gap tight">And the pleasure on your plate</p>
    <p>is <em>important</em> to you?</p>
  </div>
  <div class="front-brand">Bright Plate</div>
  <div class="front-links">
    <div class="website">brightplate-exemple.fr</div>
    <div class="socials"><span>Friendwall</span><span>Picturo</span></div>
  </div>
</section>

<section class="card card-back">
  <svg class="wave" width="520" height="520" viewBox="0 0 520 520" aria-hidden="true">
    <path d="M0,262 C40,248 80,250 120,268 C170,290 210,262 250,260 C300,258 340,305 400,303 C450,301 490,285 520,272 L520,520 L0,520 Z" fill="var(--orange)"/>
  </svg>
  <div class="back-brand">Bright Plate</div>
  <div class="person-name">MIREILLE DORAN</div>
  <div class="person-title">Dietician Nutritionist<br>Expert in Slimming and<br>Micro-Nutrition</div>
  <div class="photo-slot" role="img" aria-label="Portrait photo of Mireille Doran"></div>
  <div class="appointment">Make an appointment<br>on Rendiplan or on:</div>
  <ul class="contact-list">
    <li>
      <svg viewBox="0 0 24 24"><path fill="#fff" d="M6.6 10.8a15.1 15.1 0 0 0 6.6 6.6l2.2-2.2c.3-.3.7-.4 1-.2 1.1.4 2.3.6 3.6.6.6 0 1 .4 1 1V20c0 .6-.4 1-1 1A17 17 0 0 1 3 4c0-.6.4-1 1-1h3.5c.6 0 1 .4 1 1 0 1.3.2 2.5.6 3.6.1.3 0 .7-.2 1z"/></svg>
      06 41 58 30 92
    </li>
    <li>
      <svg viewBox="0 0 24 24"><rect x="2" y="5" width="20" height="14" fill="none" stroke="#fff" stroke-width="2"/><path d="M2 5l10 8 10-8" fill="none" stroke="#fff" stroke-width="2"/></svg>
      mireille.brightplate@exemplo-mail.fr
    </li>
    <li>
      <svg viewBox="0 0 24 24"><path fill="#fff" d="M12 2a7 7 0 0 0-7 7c0 5 7 13 7 13s7-8 7-13a7 7 0 0 0-7-7zm0 9.5A2.5 2.5 0 1 1 12 6.5a2.5 2.5 0 0 1 0 5z"/></svg>
      <span>Health Center, Rue des Glycines<br>13990 Valbelle</span>
    </li>
  </ul>
</section>

</body>
</html>
```